Square graphic for social media post

I want to create a 1080 x 1080px all-black image for the quote below that I can share on social media. I want the emphasis to be primarily on the quote, secondarily on the portrait, and third (smallest) on the logo. I want the background on the portrait to be edited so it's transparent and just shows the face of the person on a black background (no brick wall visible).

Graphic color: black
Text color: white
Content: "What we went through is going to make the greatest generation of hoteliers our industry has ever seen." << biggest text
Dorian Welk << smaller text
President, Marrowgate Hotels << smaller text
[image of person - use whichever version looks better to you]
[Add Lodging Ledger logo - whichever looks better to you]

This image needs to be readable when sized down much smaller (400x400?) so want the text and portrait to take up most of the space.

I'd like the output both as PNG and original file (preferably Canva). Thanks!

Target Market(s)

Hotel managers

Industry/Entity Type

Hospitality

Font styles to use
Sans Serif

Colors

Designer to choose colors to be used in the design.

Requirements
Must have
• Needs to focus on the quote and the person quoted (the portrait)

```html
<!DOCTYPE html>
<html lang="en">
<head>
<meta charset="utf-8">
<title>Quote Card – Dorian Welk</title>
<link href="https://fonts.googleapis.com/css2?family=Montserrat:wght@500;600;800&display=swap" rel="stylesheet">
<style>
  :root {
    --bg: #1b191a;
    --text: #ffffff;
    --portrait-light: #8a8a8a;
    --portrait-mid: #4a4a4a;
    --portrait-dark: #1b191a;
  }
  * { margin: 0; padding: 0; box-sizing: border-box; }
  html, body {
    width: 1200px;
    height: 1200px;
    overflow: hidden;
    background: var(--bg);
  }
  .card {
    position: relative;
    width: 1200px;
    height: 1200px;
    background: var(--bg);
    font-family: "Montserrat", sans-serif;
    color: var(--text);
    overflow: hidden;
  }
  .portrait {
    position: absolute;
    left: 0;
    top: 378px;
    width: 712px;
    height: 822px;
    background:
      radial-gradient(ellipse 46% 40% at 52% 38%, var(--portrait-light) 0%, var(--portrait-mid) 55%, rgba(27,25,26,0) 100%),
      radial-gradient(ellipse 70% 45% at 45% 100%, #3a3a3a 0%, #262425 60%, rgba(27,25,26,0) 100%);
  }
  .quote {
    position: absolute;
    left: 594px;
    top: 96px;
    font-weight: 800;
    font-size: 61px;
    line-height: 62px;
    letter-spacing: 0.2px;
    text-transform: uppercase;
  }
  .quote span { display: block; }
  .attribution {
    position: absolute;
    left: 0;
    width: 900px;
    top: 1056px;
    text-align: center;
    text-transform: uppercase;
  }
  .attribution-name {
    font-weight: 500;
    font-size: 25px;
    letter-spacing: 0.5px;
    line-height: 32px;
    transform: translateX(0);
    width: 900px;
    text-align: left;
    padding-left: 262px;
  }
  .attribution-title {
    font-weight: 600;
    font-size: 22px;
    letter-spacing: 0.3px;
    line-height: 34px;
    text-align: left;
    padding-left: 0;
  }
  .brand {
    position: absolute;
    left: 710px;
    top: 882px;
    width: 316px;
    display: flex;
    align-items: center;
    justify-content: center;
    gap: 12px;
  }
  .brand-dot {
    width: 12px;
    height: 12px;
    border-radius: 50%;
    background: var(--text);
  }
  .brand-name {
    font-weight: 600;
    font-size: 24px;
    letter-spacing: 3px;
    text-transform: uppercase;
  }
</style>
</head>
<body>
  <div class="card">
    <div class="portrait" role="img" aria-label="Black-and-white portrait of Dorian Welk, smiling, in a dark blazer and open-collar white shirt"></div>

    <h1 class="quote">
      <span>What we went</span>
      <span>through</span>
      <span>is going to</span>
      <span>make the</span>
      <span>greatest</span>
      <span>generation</span>
      <span>of hoteliers</span>
      <span>our industry</span>
      <span>has ever seen.</span>
    </h1>

    <div class="brand">
      <span class="brand-dot"></span>
      <span class="brand-name">Lodging Ledger</span>
    </div>

    <div class="attribution">
      <p class="attribution-name">Dorian Welk</p>
      <p class="attribution-title" style="padding-left:128px;">President, Marrowgate Hotels</p>
    </div>
  </div>
</body>
</html>
```